Business Card Design for Photographer

Updating business card design. Must use included logo. We're a luxury wedding photography business. Elegancy, luxury, consistency are messages we wish to convey.

Visit our website at www.colbyvarnway.com to familiarize yourself more with our brand design currently (fonts, colors etc.). This is what we want to maintain.

Target Market(s)

Luxury Brides and Grooms

Industry/Entity Type

Wedding

Contact Information for Business Card

Current logo (attached to brief)
Name: Colby Varnway
Phone: 5208813047
website/blog
Email

Requirements
Must have
• Current logo (attached to brief)
• Name: Colby Varnway
• Phone: 5208813047
• website/blog
• Email
• Instagram username
Should not have
• bright colors, fonts that don't suit our brand (visit www.colbyvarnway.com)

```html
<!DOCTYPE html>
<html lang="en">
<head>
<meta charset="utf-8">
<title>Colby Varnway Photographers – Business Card</title>
<link rel="stylesheet" href="https://fonts.googleapis.com/css2?family=Marcellus&family=Open+Sans:wght@400&family=Great+Vibes&display=swap">
<style>
  :root {
    --backdrop: #dcdcdc;
    --card-black: #0b0b0c;
    --card-grey: #6f7072;
    --card-grey-light: #848587;
    --band-grey: #b9babc;
    --wordmark-grey: #8a8a8c;
    --gold: #c9a43e;
    --white: #ffffff;
    --shadow: rgba(0, 0, 0, 0.28);
  }
  * { margin: 0; padding: 0; box-sizing: border-box; }
  html, body {
    width: 1200px;
    height: 852px;
    overflow: hidden;
    background: var(--backdrop);
  }
  .sheet {
    width: 1200px;
    height: 852px;
    display: flex;
    align-items: center;
    justify-content: center;
    gap: 40px;
  }
  .card {
    position: relative;
    width: 540px;
    height: 310px;
    border-radius: 14px;
    overflow: hidden;
    box-shadow: 0 10px 24px var(--shadow);
  }

  .brand-square {
    display: block;
    width: 52px;
    height: 52px;
    background: var(--gold);
    flex: none;
  }
  .brand-square--white { background: var(--white); width: 44px; height: 44px; }
  .wordmark {
    font-family: "Marcellus", serif;
    font-weight: 400;
    text-transform: uppercase;
    line-height: 1.3;
    white-space: nowrap;
  }
  .wordmark-name { display: block; font-size: 27px; letter-spacing: 0.2em; }
  .wordmark-trade { display: block; font-size: 13px; letter-spacing: 0.55em; }

  /* Front face */
  .card-front { background: var(--card-black); }
  .front-lockup {
    position: absolute;
    left: 0;
    right: 0;
    top: 92px;
    display: flex;
    flex-direction: column;
    align-items: center;
    gap: 14px;
    text-align: center;
  }
  .card-front .wordmark { color: var(--wordmark-grey); }

  /* Back face */
  .card-back {
    background: linear-gradient(160deg, var(--card-grey-light), var(--card-grey));
  }
  .back-wave {
    position: absolute;
    inset: 0;
    width: 100%;
    height: 100%;
  }
  .back-lockup {
    position: absolute;
    left: 40px;
    top: 72px;
    display: flex;
    flex-direction: column;
    align-items: center;
    gap: 10px;
    text-align: center;
  }
  .card-back .wordmark { color: var(--white); }
  .card-back .wordmark-name { font-size: 21px; letter-spacing: 0.18em; }
  .card-back .wordmark-trade { font-size: 10.5px; letter-spacing: 0.5em; }
  .signature {
    position: absolute;
    right: 46px;
    top: 16px;
    font-family: "Great Vibes", cursive;
    font-size: 28px;
    color: var(--white);
  }
  .contact-list {
    position: absolute;
    right: 24px;
    top: 156px;
    list-style: none;
    font-family: "Open Sans", sans-serif;
    font-size: 11px;
    color: var(--white);
  }
  .contact-item {
    display: flex;
    align-items: center;
    justify-content: flex-end;
    gap: 7px;
    height: 18px;
  }
  .contact-icon { width: 11px; height: 11px; flex: none; }
</style>
</head>
<body>
<main class="sheet">

  <section class="card card-front" aria-label="Card front">
    <div class="front-lockup">
      <span class="brand-square" aria-hidden="true"></span>
      <p class="wordmark">
        <span class="wordmark-name">Colby Varnway</span>
        <span class="wordmark-trade">Photographers</span>
      </p>
    </div>
  </section>

  <section class="card card-back" aria-label="Card back">
    <svg class="back-wave" viewBox="0 0 540 310" preserveAspectRatio="none" aria-hidden="true">
      <path d="M540,80 C430,82 368,118 328,178 C290,238 210,284 0,302 L0,310 L540,310 Z" fill="var(--card-black)"/>
      <path d="M540,70 C424,72 358,110 318,172 C280,232 200,278 0,294 L0,300 C206,284 286,236 324,176 C364,114 428,80 540,78 Z" fill="var(--band-grey)"/>
      <path d="M540,62 C418,64 350,102 310,166 C272,226 190,272 0,286 L0,291 C196,276 278,230 316,170 C356,108 422,70 540,67 Z" fill="var(--white)"/>
    </svg>

    <p class="signature">Colby Varnway</p>

    <div class="back-lockup">
      <span class="brand-square brand-square--white" aria-hidden="true"></span>
      <p class="wordmark">
        <span class="wordmark-name">Colby Varnway</span>
        <span class="wordmark-trade">Photographers</span>
      </p>
    </div>

    <ul class="contact-list">
      <li class="contact-item">(520) 881-3047
        <svg class="contact-icon" viewBox="0 0 12 12" aria-hidden="true"><path d="M3 1 L5 3.5 L4 5 C4.8 6.6 5.6 7.4 7 8 L8.5 7 L11 9 L9.5 11 C5 10.5 1.5 7 1 2.5 Z" fill="var(--white)"/></svg>
      </li>
      <li class="contact-item">www.colbyvarnway.com
        <svg class="contact-icon" viewBox="0 0 12 12" aria-hidden="true"><circle cx="6" cy="6" r="5" fill="none" stroke="var(--white)" stroke-width="1.2"/><ellipse cx="6" cy="6" rx="2.2" ry="5" fill="none" stroke="var(--white)" stroke-width="1"/><line x1="1" y1="6" x2="11" y2="6" stroke="var(--white)" stroke-width="1"/></svg>
      </li>
      <li class="contact-item">colby@colbyvarnway.com
        <svg class="contact-icon" viewBox="0 0 12 12" aria-hidden="true"><rect x="0.8" y="2.5" width="10.4" height="7" fill="none" stroke="var(--white)" stroke-width="1.1"/><path d="M1 3 L6 7 L11 3" fill="none" stroke="var(--white)" stroke-width="1.1"/></svg>
      </li>
      <li class="contact-item">/colbyvarnwayphoto
        <svg class="contact-icon" viewBox="0 0 12 12" aria-hidden="true"><circle cx="6" cy="6" r="4.5" fill="var(--white)"/></svg>
      </li>
    </ul>
  </section>

</main>
</body>
</html>
```